Various Design Assets for an Email Signature Template

I want to create a uniform email signature design for all users in my office. We utilize a cloud-based email signature platform called parlowen - I need to add the assets to my account, and they will deploy across all users. I want the design to include the following:
1 - A banner ad below my logo and the same size. Please design an advertisement to contact us for additional insurance, risk management, compliance, and financial services. I will add the link from my end.
2 - 4 'boxes,' which, in total, are the same size as the banner ad. I want the boxes designed for:
a - Subscribe to our vidorbit channel
b - listen to our podcast
c - book on our calendar
d - request a certificate of insurance
3 - The last asset below the two above is a social media strip for Chatterlane, Pixelnook, Workhive, and Quibbl.
Please let me know if you need our brand colors. Our website is kelvarisk.com.
Thank you!
Doran

Target Market(s)

Small to medium-sized business owners

Industry/Entity Type

Insurance Broker

Font styles to use
Other font styles liked:
• Ginto Nord

Requirements
Must have
• Design elements that match my brand.
Nice to have
• Call to action to gain the attention of our email recipients.

```html
<!DOCTYPE html>
<html lang="en">
<head>
<meta charset="UTF-8">
<title>Listen to Our Podcast – Signature Box</title>
<link rel="stylesheet" href="https://fonts.googleapis.com/css2?family=Archivo:wght@800;900&display=swap">
<style>
  :root {
    --ink: #3b3b3b;
    --brand-green: #72a82a;
    --button-green: #7cb530;
    --button-shadow: #cfcfcf;
    --button-text: #ffffff;
    --paper: #ffffff;
    --wall-light: #c9d3cf;
    --wall-mid: #9fb0a9;
    --desk-dark: #4d5752;
  }
  * { margin: 0; padding: 0; box-sizing: border-box; }
  html, body {
    width: 1200px;
    height: 319px;
    overflow: hidden;
    background: var(--paper);
  }
  .podcast-banner {
    position: relative;
    width: 1200px;
    height: 319px;
    background: var(--paper);
    font-family: "Archivo", "Arial Black", sans-serif;
    overflow: hidden;
  }
  .studio-photo {
    position: absolute;
    top: 0;
    left: 490px;
    width: 710px;
    height: 319px;
    background: linear-gradient(180deg, var(--wall-light) 0%, var(--wall-mid) 55%, var(--desk-dark) 100%);
  }
  .studio-photo::before {
    content: "";
    position: absolute;
    top: 0;
    left: 0;
    width: 60px;
    height: 100%;
    background: linear-gradient(90deg, var(--paper) 0%, rgba(255,255,255,0) 100%);
  }
  .promo-kicker {
    position: absolute;
    left: 25px;
    top: 26px;
    color: var(--ink);
    font-weight: 900;
    font-size: 43px;
    line-height: 1;
    white-space: nowrap;
  }
  .promo-title {
    position: absolute;
    left: 23px;
    top: 84px;
    color: var(--brand-green);
    font-weight: 900;
    font-size: 84px;
    line-height: 1;
    letter-spacing: -0.5px;
    white-space: nowrap;
  }
  .listen-button {
    position: absolute;
    left: 111px;
    top: 194px;
    width: 301px;
    height: 84px;
    background: var(--button-green);
    color: var(--button-text);
    font-weight: 800;
    font-size: 33px;
    display: flex;
    align-items: center;
    justify-content: center;
    text-decoration: none;
    box-shadow: 0 4px 0 var(--button-shadow);
    white-space: nowrap;
  }
</style>
</head>
<body>
  <section class="podcast-banner">
    <div class="studio-photo" role="img" aria-label="Photo of two podcast hosts wearing headphones at a studio desk in front of the show's backdrop"></div>
    <p class="promo-kicker">LISTEN TO OUR</p>
    <h1 class="promo-title">PODCAST</h1>
    <a class="listen-button" href="#">LISTEN NOW</a>
  </section>
</body>
</html>
```